Letterhead Design for Law Firm that Specializes in Property Damage Litigation

We are looking for a redesign of our letterhead. Our current letterhead lists all of our current staff members and we'd like to come up with a design that does NOT list all of the staff members so that it does not need to be updated with every newly hired employee. Must be in editable format.

We are a law firm that specializes in property damage, so we need something that is professional, yet modern. The final design should use our existing logo and should use a blue color scheme (alternate colors would be gray, black, and white).

Industry/Entity Type

Legal

Colors
0054AA
0677BA
7BADD7
CADEEF
E8F1F8

```html
<!DOCTYPE html>
<html lang="en">
<head>
<meta charset="utf-8">
<title>Hartwell Crane Morrow Letterhead</title>
<link href="https://fonts.googleapis.com/css2?family=Cinzel:wght@600&family=Montserrat:wght@800&family=Open+Sans:wght@400&display=swap" rel="stylesheet">
<style>
  :root {
    --stage: #9b9b9b;
    --paper: #ffffff;
    --brand-blue: #0a00f0;
    --band-deep: #0010ff;
    --band-mid: #0066ff;
    --band-glow: #00f2ff;
    --band-line: #2f5cff;
    --on-band: #ffffff;
    --icon-ink: #1a3cff;
  }
  * { margin: 0; padding: 0; box-sizing: border-box; }
  html, body { width: 901px; height: 1200px; overflow: hidden; }
  body { background: var(--stage); position: relative; }

  .letterhead {
    position: absolute; left: 74px; top: 68px;
    width: 752px; height: 1063px;
    background: var(--paper);
    overflow: hidden;
  }

  .brand { position: absolute; left: 39px; top: 46px; }
  .brand-square {
    position: absolute; left: 0; top: 22px;
    width: 52px; height: 52px; background: var(--brand-blue);
  }
  .brand-name {
    position: absolute; left: 128px; top: 0;
    font-family: "Cinzel", serif; font-weight: 600;
    font-size: 34px; line-height: 32px; color: var(--brand-blue);
    white-space: nowrap;
  }

  .contact-band {
    position: absolute; left: 0; top: 881px;
    width: 752px; height: 182px;
    background:
      radial-gradient(circle at 100% 0%, var(--band-glow) 0, rgba(0,242,255,0.55) 90px, rgba(0,242,255,0) 260px),
      linear-gradient(90deg, var(--band-deep) 0%, var(--band-mid) 65%, #0a8cff 100%);
    color: var(--on-band);
  }
  .band-line {
    position: absolute; left: 0; top: 10px;
    width: 360px; height: 2px; background: var(--band-line);
  }
  .offices { position: absolute; left: 25px; top: 27px; }
  .office-title {
    font-family: "Montserrat", sans-serif; font-weight: 800;
    font-size: 12.5px; line-height: 16px; margin-left: 3px; letter-spacing: 0.1px;
  }
  .office + .office { margin-top: 3px; }
  .contact-line {
    display: flex; align-items: center; gap: 4px;
    font-family: "Open Sans", sans-serif; font-weight: 400;
    font-size: 12.6px; line-height: 14.5px; white-space: nowrap;
  }
  .contact-line svg { width: 10px; height: 10px; flex: none; }
</style>
</head>
<body>
  <main class="letterhead">
    <header class="brand">
      <div class="brand-square"></div>
      <div class="brand-name">HARTWELL<br>CRANE<br>MORROW</div>
    </header>

    <footer class="contact-band">
      <div class="band-line"></div>
      <div class="offices">
        <section class="office">
          <h2 class="office-title">PHILADELPHIA OFFICE</h2>
          <p class="contact-line">
            <svg viewBox="0 0 10 10" aria-hidden="true"><circle cx="5" cy="5" r="5" fill="#fff"/><path d="M3.3 2.4l1 1-.5.6a3 3 0 0 0 1.7 1.7l.6-.5 1 1-.7.8C4.6 7 3 5.4 2.6 3.3z" fill="var(--icon-ink)"/></svg>
            215.555.0140
          </p>
          <p class="contact-line">
            <svg viewBox="0 0 10 10" aria-hidden="true"><circle cx="5" cy="5" r="5" fill="#fff"/><rect x="2.6" y="4" width="4.8" height="3" rx="0.6" fill="var(--icon-ink)"/><rect x="2.2" y="2.8" width="5.6" height="1.2" rx="0.5" fill="var(--icon-ink)"/></svg>
            215.555.0177
          </p>
          <p class="contact-line">
            <svg viewBox="0 0 10 10" aria-hidden="true"><circle cx="5" cy="5" r="5" fill="#fff"/><path d="M5 2a2 2 0 0 1 2 2c0 1.5-2 3.8-2 3.8S3 5.5 3 4a2 2 0 0 1 2-2z" fill="var(--icon-ink)"/><circle cx="5" cy="4" r="0.7" fill="#fff"/></svg>
            2200 Arch Street Suite 840 Philadelphia, PA 19103
          </p>
        </section>
        <section class="office">
          <h2 class="office-title">NEW JERSEY OFFICE</h2>
          <p class="contact-line">
            <svg viewBox="0 0 10 10" aria-hidden="true"><circle cx="5" cy="5" r="5" fill="#fff"/><path d="M3.3 2.4l1 1-.5.6a3 3 0 0 0 1.7 1.7l.6-.5 1 1-.7.8C4.6 7 3 5.4 2.6 3.3z" fill="var(--icon-ink)"/></svg>
            856.555.0162
          </p>
          <p class="contact-line">
            <svg viewBox="0 0 10 10" aria-hidden="true"><circle cx="5" cy="5" r="5" fill="#fff"/><rect x="2.6" y="4" width="4.8" height="3" rx="0.6" fill="var(--icon-ink)"/><rect x="2.2" y="2.8" width="5.6" height="1.2" rx="0.5" fill="var(--icon-ink)"/></svg>
            215.555.0177
          </p>
          <p class="contact-line">
            <svg viewBox="0 0 10 10" aria-hidden="true"><circle cx="5" cy="5" r="5" fill="#fff"/><path d="M5 2a2 2 0 0 1 2 2c0 1.5-2 3.8-2 3.8S3 5.5 3 4a2 2 0 0 1 2-2z" fill="var(--icon-ink)"/><circle cx="5" cy="4" r="0.7" fill="#fff"/></svg>
            415 Marlton Pike East Suite 310 Cherry Hill, NJ 08034
          </p>
          <p class="contact-line">
            <svg viewBox="0 0 10 10" aria-hidden="true"><circle cx="5" cy="5" r="5" fill="#fff"/><circle cx="5" cy="5" r="3" fill="none" stroke="var(--icon-ink)" stroke-width="0.8"/><ellipse cx="5" cy="5" rx="1.3" ry="3" fill="none" stroke="var(--icon-ink)" stroke-width="0.7"/><path d="M2 5h6" stroke="var(--icon-ink)" stroke-width="0.7"/></svg>
            www.hcmlegal.com
          </p>
        </section>
      </div>
    </footer>
  </main>
</body>
</html>
```